Redesign Application Page for Job Position

Would like to get a redesign on our Job Application Page.
You can use brennoxguard or valmoreta as references.

http://www.careersatklv.example/KLV/NCreateAccount.aspx?aga=qwtrzx4hemLK7

Target Market(s)

Professional Security Individuals

Industry/Entity Type

Security Guard

Coding

Coded - Design and coding required

Number of Pages Required

1 page

Font styles to use
Sans Serif

Colors
0255a3
3276b5
ffcf3e
fee18a

Requirements
Must have
• User Friendly, Easy Navigation. Must be very easy to read and understand what is required or missing.
Should not have
• Ugly or Bulky

```html
<!DOCTYPE html>
<html lang="en">
<head>
<meta charset="utf-8">
<title>Kelvane Guard Services, Inc. — Create an Application</title>
<link href="https://fonts.googleapis.com/css2?family=Oswald:wght@400;500&family=Montserrat:wght@400;500&display=swap" rel="stylesheet">
<style>
:root{
  --navy:#221d4a;
  --gold:#efc40f;
  --gold-text:#f2c51a;
  --page:#f2f2f3;
  --field:#ffffff;
  --line:#d4d4d8;
  --ink:#1f1c3d;
  --red:#d0202a;
  --muted:#3a3a4a;
}
*{box-sizing:border-box;margin:0;padding:0}
html,body{width:964px;height:1200px;overflow:hidden}
body{background:var(--page);font-family:'Montserrat',sans-serif;color:var(--ink);position:relative}
.site-header{position:absolute;left:0;top:0;width:964px;height:195px;background:var(--navy);text-align:center}
.brand-mark{position:absolute;left:457px;top:28px;width:50px;height:50px;border-radius:50%;background:var(--gold)}
.brand-name{position:absolute;left:0;right:0;top:114px;font-family:'Oswald',sans-serif;font-weight:500;font-size:30px;letter-spacing:1.6px;color:var(--gold-text)}
.page-title{position:absolute;left:0;right:0;top:154px;font-family:'Oswald',sans-serif;font-size:19px;letter-spacing:1.4px;color:#fff}
.notice-bar{position:absolute;left:0;top:195px;width:964px;height:33px;background:var(--gold);font-family:'Oswald',sans-serif;box-shadow:0 2px 3px rgba(0,0,0,.15)}
.notice-text{position:absolute;left:69px;top:7px;font-size:14px;letter-spacing:.6px;color:var(--navy)}
.notice-date{position:absolute;right:69px;top:9px;font-size:11.5px;letter-spacing:.6px;color:#fff}
.field-label{position:absolute;font-family:'Oswald',sans-serif;font-size:12px;letter-spacing:.8px;color:var(--ink)}
.req{color:var(--red)}
.text-input{position:absolute;height:28px;background:var(--field);border:1px solid var(--line)}
.select{position:absolute;height:28px;background:var(--field);border:1px solid var(--line);font-size:11px;color:var(--muted);padding:8px 0 0 13px}
.select svg{position:absolute;right:12px;top:11px}
.inline-label{position:absolute;font-size:11px;font-weight:500}
.radio{position:absolute;font-size:11px;font-weight:500;display:flex;align-items:center;gap:5px}
.dot{width:10px;height:10px;border-radius:50%;background:var(--ink);display:inline-block}
.dot.on{background:var(--gold);border:2.5px solid var(--navy)}
.data-table{position:absolute;border-collapse:collapse;background:#fff;font-size:11px;font-weight:500}
.data-table th{background:var(--gold);font-family:'Oswald',sans-serif;font-weight:400;font-size:11.5px;letter-spacing:.8px;text-align:left;height:28px;padding-left:13px;color:var(--navy)}
.data-table td{border:1px solid #e1e1e4;height:27.5px;padding-left:13px}
.license-table .expire{color:var(--muted);font-weight:400;font-size:10.5px}
.license-table .expire svg{vertical-align:-1px;margin-left:5px}
.shift-table th.day,.shift-table td.day{text-align:center;padding-left:0}
.shift-table td{height:28px}
.btn{position:absolute;top:1098px;width:120px;height:28px;font-family:'Oswald',sans-serif;font-size:13px;letter-spacing:2.2px;text-align:center;line-height:26px}
.btn-primary{left:69px;background:var(--navy);color:#fff;border:1px solid var(--navy)}
.btn-secondary{left:203px;background:#fff;color:var(--navy);border:1.5px solid var(--navy)}
.hero-photo{position:absolute;left:700px;top:258px;width:244px;height:886px;border-radius:60px 60px 30px 30px;background:linear-gradient(180deg,#c9d9ec 0%,#b7cde6 40%,#2c3c6e 55%,#22315e 92%,#1a1a22 100%)}
.site-footer{position:absolute;left:0;top:1161px;width:964px;height:39px;background:var(--navy);font-family:'Oswald',sans-serif;font-size:11.5px;letter-spacing:.7px;color:#fff}
.help{position:absolute;left:69px;top:12px}
.copyright{position:absolute;right:69px;top:12px}
</style>
</head>
<body>
<header class="site-header">
  <span class="brand-mark"></span>
  <h1 class="brand-name">KELVANE GUARD SERVICES, INC.</h1>
  <h2 class="page-title">CREATE AN APPLICATION</h2>
</header>
<div class="notice-bar">
  <p class="notice-text">Complete all required fields (Star Mark), then click "Continue" to create your account!</p>
  <p class="notice-date">Date Created:&nbsp; 11 January, 2018</p>
</div>

<main class="application-form">
  <label class="field-label" style="left:69px;top:260px">First Name <span class="req">*</span></label>
  <div class="text-input" style="left:69px;top:283px;width:191px"></div>
  <label class="field-label" style="left:281px;top:260px">Middle Name</label>
  <div class="text-input" style="left:281px;top:283px;width:191px"></div>
  <label class="field-label" style="left:492px;top:260px">Last Name <span class="req">*</span></label>
  <div class="text-input" style="left:492px;top:283px;width:191px"></div>

  <label class="field-label" style="left:69px;top:322px">Gender</label>
  <span class="radio" style="left:70px;top:347px"><i class="dot on"></i>Male</span>
  <span class="radio" style="left:139px;top:347px"><i class="dot"></i>Female</span>
  <label class="field-label" style="left:281px;top:322px">Date of Birth</label>
  <div class="select" style="left:281px;top:345px;width:90px">Month<svg width="7" height="5" viewBox="0 0 7 5"><path d="M1 1l2.5 2.5L6 1" stroke="#333" fill="none"/></svg></div>
  <div class="select" style="left:378px;top:345px;width:90px">Day<svg width="7" height="5" viewBox="0 0 7 5"><path d="M1 1l2.5 2.5L6 1" stroke="#333" fill="none"/></svg></div>
  <div class="select" style="left:474px;top:345px;width:90px">Year<svg width="7" height="5" viewBox="0 0 7 5"><path d="M1 1l2.5 2.5L6 1" stroke="#333" fill="none"/></svg></div>

  <label class="field-label" style="left:69px;top:384px">Street Address <span class="req">*</span></label>
  <div class="text-input" style="left:69px;top:407px;width:191px"></div>
  <label class="field-label" style="left:281px;top:384px">City</label>
  <div class="text-input" style="left:281px;top:407px;width:191px"></div>
  <label class="field-label" style="left:492px;top:384px">State</label>
  <div class="select" style="left:492px;top:407px;width:191px">Select<svg width="7" height="5" viewBox="0 0 7 5"><path d="M1 1l2.5 2.5L6 1" stroke="#333" fill="none"/></svg></div>

  <label class="field-label" style="left:69px;top:447px">Nearest Office</label>
  <div class="select" style="left:69px;top:470px;width:191px">Select<svg width="7" height="5" viewBox="0 0 7 5"><path d="M1 1l2.5 2.5L6 1" stroke="#333" fill="none"/></svg></div>
  <label class="field-label" style="left:281px;top:447px">Zip <span class="req">*</span></label>
  <div class="text-input" style="left:281px;top:470px;width:191px"></div>
  <label class="field-label" style="left:492px;top:447px">Job Position</label>
  <div class="select" style="left:492px;top:470px;width:191px">Select<svg width="7" height="5" viewBox="0 0 7 5"><path d="M1 1l2.5 2.5L6 1" stroke="#333" fill="none"/></svg></div>

  <label class="field-label" style="left:69px;top:509px">Phone Number</label>
  <span class="inline-label" style="left:69px;top:540px">Cell</span>
  <div class="text-input" style="left:96px;top:532px;width:164px"></div>
  <span class="inline-label" style="left:282px;top:540px">Phone</span>
  <div class="text-input" style="left:323px;top:532px;width:148px"></div>
  <label class="field-label" style="left:492px;top:509px">SSN</label>
  <div class="text-input" style="left:492px;top:532px;width:191px"></div>

  <label class="field-label" style="left:69px;top:573px">License Details</label>
  <table class="data-table license-table" style="left:69px;top:595px;width:614px">
    <thead><tr><th style="width:301px">TYPE</th><th style="width:196px">NUMBER</th><th>EXPIRE DETAILS</th></tr></thead>
    <tbody>
      <tr><td>Guard card</td><td></td><td class="expire">(mm/dd/yyyy)<svg width="10" height="10" viewBox="0 0 10 10"><rect x="0.5" y="1.5" width="9" height="8" fill="none" stroke="#333"/><path d="M0.5 3.5h9M3 5v4M6 5v4M0.5 6.5h9" stroke="#333" stroke-width=".8"/></svg></td></tr>
      <tr><td>Baton</td><td></td><td class="expire">(mm/dd/yyyy)<svg width="10" height="10" viewBox="0 0 10 10"><rect x="0.5" y="1.5" width="9" height="8" fill="none" stroke="#333"/><path d="M0.5 3.5h9M3 5v4M6 5v4M0.5 6.5h9" stroke="#333" stroke-width=".8"/></svg></td></tr>
      <tr><td>Gun Permit</td><td></td><td class="expire">(mm/dd/yyyy)<svg width="10" height="10" viewBox="0 0 10 10"><rect x="0.5" y="1.5" width="9" height="8" fill="none" stroke="#333"/><path d="M0.5 3.5h9M3 5v4M6 5v4M0.5 6.5h9" stroke="#333" stroke-width=".8"/></svg></td></tr>
      <tr><td>Transportation Workers Identification Card (TWIC)</td><td></td><td class="expire">(mm/dd/yyyy)<svg width="10" height="10" viewBox="0 0 10 10"><rect x="0.5" y="1.5" width="9" height="8" fill="none" stroke="#333"/><path d="M0.5 3.5h9M3 5v4M6 5v4M0.5 6.5h9" stroke="#333" stroke-width=".8"/></svg></td></tr>
      <tr><td>Merchant Mariner Credential (MMC)</td><td></td><td class="expire">(mm/dd/yyyy)<svg width="10" height="10" viewBox="0 0 10 10"><rect x="0.5" y="1.5" width="9" height="8" fill="none" stroke="#333"/><path d="M0.5 3.5h9M3 5v4M6 5v4M0.5 6.5h9" stroke="#333" stroke-width=".8"/></svg></td></tr>
      <tr><td style="height:45px;line-height:17px">Standards of Training, Certification and<br>Watchkeeping for Seafarers (SCTW)</td><td></td><td class="expire">(mm/dd/yyyy)<svg width="10" height="10" viewBox="0 0 10 10"><rect x="0.5" y="1.5" width="9" height="8" fill="none" stroke="#333"/><path d="M0.5 3.5h9M3 5v4M6 5v4M0.5 6.5h9" stroke="#333" stroke-width=".8"/></svg></td></tr>
    </tbody>
  </table>

  <label class="field-label" style="left:69px;top:818px">ID Document Type</label>
  <div class="select" style="left:69px;top:841px;width:191px">Select<svg width="7" height="5" viewBox="0 0 7 5"><path d="M1 1l2.5 2.5L6 1" stroke="#333" fill="none"/></svg></div>
  <label class="field-label" style="left:281px;top:818px">Additional Languages</label>
  <span class="radio" style="left:282px;top:843px"><i class="dot on"></i>Spanish</span>
  <span class="radio" style="left:351px;top:843px"><i class="dot"></i>French</span>
  <span class="radio" style="left:414px;top:843px"><i class="dot"></i>Japanese</span>
  <span class="radio" style="left:492px;top:843px"><i class="dot"></i>Chinese</span>

  <label class="field-label" style="left:69px;top:880px">Email <span class="req">*</span></label>
  <div class="text-input" style="left:69px;top:903px;width:191px"></div>
  <label class="field-label" style="left:281px;top:880px">How did you hear about us?</label>
  <div class="select" style="left:281px;top:903px;width:191px">Select<svg width="7" height="5" viewBox="0 0 7 5"><path d="M1 1l2.5 2.5L6 1" stroke="#333" fill="none"/></svg></div>

  <label class="field-label" style="left:69px;top:942px">Work Availability</label>
  <table class="data-table shift-table" style="left:69px;top:965px;width:614px">
    <thead><tr><th>SHIFT</th><th class="day" style="width:49px">SUN</th><th class="day" style="width:49px">MON</th><th class="day" style="width:49px">TUE</th><th class="day" style="width:49px">WED</th><th class="day" style="width:49px">THU</th><th class="day" style="width:49px">FRI</th><th class="day" style="width:49px">SAT</th></tr></thead>
    <tbody>
      <tr><td>Day Shift</td><td class="day"><i class="dot on"></i></td><td class="day"><i class="dot"></i></td><td class="day"><i class="dot"></i></td><td class="day"><i class="dot"></i></td><td class="day"><i class="dot"></i></td><td class="day"><i class="dot"></i></td><td class="day"><i class="dot"></i></td></tr>
      <tr><td>Swing Shift</td><td class="day"><i class="dot"></i></td><td class="day"><i class="dot"></i></td><td class="day"><i class="dot"></i></td><td class="day"><i class="dot"></i></td><td class="day"><i class="dot"></i></td><td class="day"><i class="dot"></i></td><td class="day"><i class="dot"></i></td></tr>
      <tr><td>Night Shift</td><td class="day"><i class="dot"></i></td><td class="day"><i class="dot"></i></td><td class="day"><i class="dot"></i></td><td class="day"><i class="dot"></i></td><td class="day"><i class="dot"></i></td><td class="day"><i class="dot"></i></td><td class="day"><i class="dot"></i></td></tr>
    </tbody>
  </table>

  <span class="btn btn-primary">CONTINUE</span>
  <span class="btn btn-secondary">DISCARD</span>
</main>

<div class="hero-photo" role="img" aria-label="Photo of a uniformed security guard in a light blue shirt and navy trousers holding a radio"></div>

<footer class="site-footer">
  <p class="help">Need Help?&nbsp; Call us at: (310)555-0148 and ask for a Human Resource representative.</p>
  <p class="copyright">Copyright © 2018&nbsp; I&nbsp; All Rights Reserved.</p>
</footer>
</body>
</html>
```